Business Card Design

We are a design build firm specializing in the construction and design of kitchens. We are a "green" company, hence the logo. Here are some IDEAS we came up with. I am asking to use this for every person in our firm, so I will need to be able to edit the text. On the back, I am thinking of a very simple design... maybe carry over the white band around the edge. Maybe a simple saying on the back "Crafting kitchens from first sketch to final finish".

Please see our current website for our style and design info
www.cabinetrefitexample.com (going to be forwarded to pinelanternllc.com)

Industry/Entity Type

Construction

Contact Information for Business Card

Pine Lantern Design & Construction
Moira Faddenby - Chief Designer
418 Willow Bend
Alderbrook, ME 06712
203.555.0147 C
203.555.0192 O
www.pinelanternllc.com
plcabinets@mailbox.example

```html
<!DOCTYPE html>
<html lang="en">
<head>
<meta charset="utf-8">
<title>Pine Lantern Design &amp; Construction – Business Card</title>
<link rel="stylesheet" href="https://fonts.googleapis.com/css2?family=Jost:ital,wght@0,300;0,400;0,500;0,700;1,300&display=swap">
<style>
  :root {
    --stage: #2b2b2b;
    --green: #7cbb3a;
    --ink: #1f2a22;
    --white: #ffffff;
    --grey-dark: #55575a;
    --grey-light: #b3b5b8;
  }
  * { box-sizing: border-box; margin: 0; padding: 0; }
  html, body {
    width: 1200px; height: 900px; overflow: hidden;
    background: var(--stage);
    font-family: "Jost", "Futura", sans-serif;
  }
  .canvas {
    width: 1200px; height: 900px;
    display: flex; flex-direction: column;
    align-items: center; justify-content: center; gap: 40px;
  }
  .card {
    position: relative;
    width: 665px; height: 380px;
    overflow: hidden;
    box-shadow: 0 10px 30px rgba(0,0,0,.45);
  }
  .card__bg { position: absolute; inset: 0; width: 100%; height: 100%; }

  .brand {
    position: absolute;
    display: flex; align-items: center; gap: 12px;
  }
  .brand__dot {
    width: 26px; height: 26px; border-radius: 50%;
    background: var(--green);
    flex: none;
  }
  .brand__name {
    font-weight: 500;
    color: var(--ink);
    font-size: 25px;
    letter-spacing: .06em;
    text-transform: uppercase;
    line-height: 1.15;
  }
  .brand__rule {
    position: absolute;
    height: 2px;
    background: var(--grey-dark);
  }

  .card--front .brand { left: 150px; top: 70px; }
  .card--front .brand__rule { left: 150px; top: 150px; width: 380px; transform: rotate(-3deg); transform-origin: left; opacity: .6; }

  .person {
    position: absolute; left: 42px; top: 250px;
    color: var(--white);
  }
  .person__name {
    font-weight: 700; font-size: 21px; letter-spacing: .04em;
    text-transform: uppercase; color: var(--ink);
    line-height: 1;
  }
  .person__title {
    font-weight: 300; font-style: italic; font-size: 18px;
    margin-top: 4px;
  }
  .person__address {
    font-style: normal; font-weight: 400; font-size: 20px;
    line-height: 1.1; margin-top: 16px;
  }

  .contact {
    position: absolute; right: 34px; top: 166px;
    color: var(--white); text-align: right;
    font-size: 18px; font-weight: 400; line-height: 1.12;
  }
  .contact__phones { list-style: none; margin-bottom: 18px; }
  .contact__phones li { display: flex; justify-content: flex-end; align-items: center; gap: 8px; }
  .contact__tag {
    font-weight: 700; font-size: 13px; color: var(--white);
    width: 14px; text-align: center;
  }

  .card--back .brand { left: 130px; top: 135px; }
  .card--back .brand__rule { left: 60px; top: 205px; width: 540px; background: var(--grey-light); opacity: .8; }
  .tagline {
    position: absolute; left: 0; right: 0; top: 225px;
    text-align: center;
    color: var(--white);
    font-weight: 400; font-size: 17px; letter-spacing: .1em;
    text-transform: uppercase;
  }
</style>
</head>
<body>
<main class="canvas">

  <section class="card card--front" aria-label="Business card front">
    <svg class="card__bg" viewBox="0 0 665 380" preserveAspectRatio="none" aria-hidden="true">
      <defs>
        <radialGradient id="paperGlow" cx="0.55" cy="0.1" r="0.8">
          <stop offset="0" stop-color="#ffffff"/>
          <stop offset="1" stop-color="#c4c6c8"/>
        </radialGradient>
        <radialGradient id="greenGlow" cx="0.5" cy="0.35" r="0.8">
          <stop offset="0" stop-color="#8dc63f"/>
          <stop offset="1" stop-color="#6aa532"/>
        </radialGradient>
      </defs>
      <rect width="665" height="380" fill="url(#paperGlow)"/>
      <path d="M0 215 C 200 225 430 195 665 120 L665 380 L0 380 Z" fill="url(#greenGlow)"/>
    </svg>

    <div class="brand">
      <span class="brand__dot" aria-hidden="true"></span>
      <span class="brand__name">Pine Lantern<br>Design &amp; Construction</span>
    </div>
    <span class="brand__rule" aria-hidden="true"></span>

    <div class="person">
      <p class="person__name">Moira Faddenby</p>
      <p class="person__title">Chief Designer</p>
      <address class="person__address">418 Willow Bend<br>Alderbrook, ME 06712</address>
    </div>

    <div class="contact">
      <ul class="contact__phones">
        <li><span class="contact__tag">C</span>203.555.0147</li>
        <li><span class="contact__tag">O</span>203.555.0192</li>
      </ul>
      <p>moira@pinelanternllc.com</p>
      <p>www.pinelanternllc.com</p>
    </div>
  </section>

  <section class="card card--back" aria-label="Business card back">
    <svg class="card__bg" viewBox="0 0 665 380" preserveAspectRatio="none" aria-hidden="true">
      <defs>
        <radialGradient id="slateGlow" cx="0.6" cy="0.05" r="0.95">
          <stop offset="0" stop-color="#9a9c9f"/>
          <stop offset="0.5" stop-color="#77797c"/>
          <stop offset="1" stop-color="#4f5154"/>
        </radialGradient>
      </defs>
      <rect width="665" height="380" fill="url(#slateGlow)"/>
    </svg>

    <div class="brand">
      <span class="brand__dot" aria-hidden="true"></span>
      <span class="brand__name">Pine Lantern<br>Design &amp; Construction</span>
    </div>
    <span class="brand__rule" aria-hidden="true"></span>
    <p class="tagline">Crafting kitchens from first sketch to final finish</p>
  </section>

</main>
</body>
</html>
```